Business Card Design

This is a new business to be run from my home. I have attended certificate workshops run by Dr Kevin Ruddock who is a Master Trainer in Gentle Flow for Mobility.
I wish to communicate to people that Tai Chi is for everyone, no matter their age, gender or fitness levels. Tai Chi is taught both standing & seated.
The card should have a slightly Asian feel, mainly printed in black & white with perhaps a little soft pink &/or green.

Target Market(s)

people of all ages from 10 years up, poor fitness & mild disabilities.

Industry/Entity Type

Fitness

Contact Information for Business Card

Marrowdene Flowing Arts for Body, Mind & Stillness

Brenna Holcroft, Certificated Leader

ph 5281 9046

Requirements
Nice to have
• a feeling of health & peace.
Should not have
• bright colours, fancy fonts

```html
<!DOCTYPE html>
<html lang="en">
<head>
<meta charset="utf-8">
<title>Marrowdene Flowing Arts – Business Card</title>
<link rel="stylesheet" href="https://fonts.googleapis.com/css2?family=Black+Ops+One&family=Source+Sans+3:wght@400&display=swap">
<style>
  :root {
    --page: #ffffff;
    --green-top: #2f8a55;
    --green-mid: #3f9862;
    --green-deep: #2a6443;
    --band-top: #92203f;
    --band-bottom: #c83d66;
    --title-blue: #2f5db0;
    --title-edge: #ffffff;
    --title-shadow: #0f2a1a;
    --text-light: #f1f1ee;
    --text-gold: #f3c43a;
    --phone-grey: #e6e1e2;
    --mark-blue: #2a63b8;
    --veil: rgba(200, 230, 205, 0.14);
  }
  * { margin: 0; padding: 0; box-sizing: border-box; }
  html, body {
    width: 1200px; height: 741px; overflow: hidden;
    background: var(--page);
  }
  .card {
    position: absolute; left: 46px; top: 46px;
    width: 1113px; height: 649px;
    background: linear-gradient(180deg, var(--green-top) 0%, var(--green-mid) 45%, var(--green-deep) 84%);
    overflow: hidden;
    font-family: "Source Sans 3", "Myriad Pro", sans-serif;
  }
  .card__flourish {
    position: absolute; left: 95px; top: 24px;
    width: 340px; height: 505px;
    border-radius: 45% 55% 40% 60%;
    background: radial-gradient(ellipse at 50% 45%, var(--veil), rgba(200,230,205,0) 70%);
  }
  .card__title {
    position: absolute; left: 22px; top: 30px;
    width: 1070px; height: 80px;
    filter: drop-shadow(3px 5px 3px var(--title-shadow));
  }
  .card__title text {
    font-family: "Black Ops One", "Arial Black", sans-serif;
    font-size: 60px;
    fill: var(--title-blue);
    stroke: var(--title-edge);
    stroke-width: 3px;
    paint-order: stroke fill;
  }
  .card__tagline {
    position: absolute; left: 43px; top: 372px;
    font-size: 48px; color: var(--text-light);
    white-space: nowrap; letter-spacing: -0.3px;
  }
  .card__role {
    position: absolute; left: 198px; top: 448px;
    font-size: 48px; color: var(--text-gold);
    white-space: nowrap;
    text-shadow: 1px 2px 2px rgba(0,0,0,0.35);
  }
  .card__brand {
    position: absolute; left: 790px; top: 178px;
    display: flex; flex-direction: column; align-items: center; gap: 18px;
  }
  .card__brand-dot {
    width: 72px; height: 72px; border-radius: 50%;
    background: var(--mark-blue);
  }
  .card__brand-name {
    font-size: 46px; color: var(--text-light);
  }
  .card__band {
    position: absolute; left: 0; bottom: 0;
    width: 100%; height: 100px;
    background: linear-gradient(180deg, var(--band-top), var(--band-bottom));
  }
  .card__phone {
    position: absolute; left: 415px; top: 20px;
    font-size: 48px; color: var(--phone-grey);
    white-space: nowrap;
    text-shadow: 1px 2px 2px rgba(0,0,0,0.45);
  }
</style>
</head>
<body>
  <main class="card">
    <div class="card__flourish" role="img" aria-label="Faint decorative flowing vine flourish"></div>

    <svg class="card__title" viewBox="0 0 1070 80" aria-label="Marrowdene Flowing Arts for Body">
      <text x="4" y="64" textLength="1060" lengthAdjust="spacingAndGlyphs">MARROWDENE FLOWING ARTS FOR BODY</text>
    </svg>

    <div class="card__brand">
      <span class="card__brand-dot"></span>
      <span class="card__brand-name">Marrowdene</span>
    </div>

    <p class="card__tagline">Mind &amp; Stillness Brenna Holcroft</p>
    <p class="card__role">Certificated Leader</p>

    <footer class="card__band">
      <p class="card__phone">Ph :&nbsp; 5281 9046</p>
    </footer>
  </main>
</body>
</html>
```